wandervelo.net
"Where Every Road Begins"
wandervelo.net - Travel
Creative Brief
Professional
"Where Every Road Begins" (our slogan)
48/3 Sukprasert raod,Thonlamai. Bangkok 10400 (we want this on the back of the business card, not the front)
wandervelo@mailbox-example.net
We would like the front of the business card to be very simple – company colours, name, logo & slogan. As you can see from above we would also like to keep the business card as modern & professional as possible, too (please refer to our website www.wandervelo.net). Question: Will we be able to edit the employee names on the business cards when the project is complete? Thanks.
Siriporn Laemchabangkul 48/3 Sukprasert raod,Thonlamai. Bangkok 10400 Tel .025194638 Fax.025194637 Mobile: 0863150472 Email:wandervelo@mailbox-example.net Website: wandervelo.net www.wandervelo.net

```html
<!DOCTYPE html>
<html lang="en">
<head>
<meta charset="utf-8">
<title>wandervelo.net — Stationery Set</title>
<link rel="stylesheet" href="https://fonts.googleapis.com/css2?family=Open+Sans:ital,wght@0,400;0,700;1,400&display=swap">
<style>
  :root {
    --bg-top: #5a5a5a;
    --bg-bottom: #2f2f2f;
    --brand-green: #1b4a3d;
    --brand-orange: #e8771f;
    --paper: #ffffff;
    --paper-shade: #ececec;
    --ink-light: #ffffff;
    --ink-muted: #c9d2ce;
    --ink-dark: #3b3b3b;
  }
  html, body { margin: 0; padding: 0; width: 1200px; height: 302px; overflow: hidden; }
  body {
    background: linear-gradient(180deg, var(--bg-top), var(--bg-bottom));
    font-family: "Open Sans", Arial, sans-serif;
  }
  .stationery { display: block; width: 1200px; height: 302px; }
  .green { fill: var(--brand-green); }
  .orange { fill: var(--brand-orange); }
  .paper { fill: var(--paper); }
  .paper-shade { fill: var(--paper-shade); }
  .swoosh { fill: none; stroke: var(--brand-orange); }
  .flap-line { fill: none; stroke: var(--brand-green); stroke-width: 1; }
  .wordmark { font-family: "Open Sans", Arial, sans-serif; font-weight: 700; }
  .wordmark--light { fill: var(--ink-light); }
  .wordmark--dark { fill: var(--brand-green); }
  .tagline { font-style: italic; fill: var(--ink-light); }
  .tagline--dark { font-style: italic; fill: var(--ink-dark); }
  .caption { fill: var(--ink-muted); }
  .detail { fill: var(--ink-light); }
  .name { font-weight: 700; fill: var(--ink-light); }
</style>
</head>
<body>
<svg class="stationery" viewBox="0 0 1200 302" xmlns="http://www.w3.org/2000/svg">

  <!-- Brand heading -->
  <g class="brand-heading">
    <text class="wordmark wordmark--light" x="91" y="36" font-size="22">wandervelo.net</text>
    <text class="tagline" x="112" y="49" font-size="8.5">"Where Every Road Begins"</text>
    <text class="caption" x="130" y="62" font-size="5.5">Travel Identity Set</text>
  </g>

  <!-- Business card: front -->
  <g class="card card--front" transform="translate(29,113)">
    <rect class="green" width="91" height="46"/>
    <path class="orange" d="M56 0 H91 V46 H66 C76 32 56 18 56 0 Z"/>
    <text class="wordmark wordmark--light" x="6" y="17" font-size="6">wandervelo.net</text>
    <text class="tagline" x="6" y="23" font-size="3.2">"Where Every Road Begins"</text>
  </g>

  <!-- Business card: back -->
  <g class="card card--back" transform="translate(125,113)">
    <rect class="green" width="91" height="46"/>
    <path class="orange" d="M0 0 H30 C22 14 40 32 26 46 H0 Z"/>
    <text class="name" x="38" y="12" font-size="4">Contact Name</text>
    <text class="detail" x="38" y="19" font-size="2.8">Office address line</text>
    <text class="detail" x="38" y="24" font-size="2.8">Tel · Fax · Mobile</text>
    <text class="detail" x="38" y="29" font-size="2.8">Email · Website</text>
  </g>

  <!-- Business card: light variant -->
  <g class="card card--light" transform="translate(106,204)">
    <rect class="paper-shade" width="110" height="38"/>
    <text class="wordmark wordmark--dark" x="55" y="18" font-size="7.5" text-anchor="middle">wandervelo.net</text>
    <text class="tagline--dark" x="55" y="25" font-size="3.2" text-anchor="middle">"Where Every Road Begins"</text>
  </g>

  <!-- Letterhead, page one -->
  <g class="letterhead" transform="translate(295,19)">
    <rect class="paper" width="159" height="257"/>
    <path class="green" d="M0 0 H159 V22 C110 36 55 16 0 28 Z"/>
    <path class="swoosh" stroke-width="1.6" d="M0 31 C55 19 110 39 159 25"/>
    <text class="wordmark wordmark--light" x="8" y="12" font-size="6">wandervelo.net</text>
    <text class="detail" x="100" y="8" font-size="2.6">Office address line</text>
    <text class="detail" x="100" y="12" font-size="2.6">Phone and fax</text>
    <text class="detail" x="100" y="16" font-size="2.6">Web address</text>
  </g>

  <!-- Letterhead, page two -->
  <g class="letterhead" transform="translate(499,19)">
    <rect class="paper" width="159" height="257"/>
    <path class="green" d="M0 0 H159 V22 C110 36 55 16 0 28 Z"/>
    <path class="swoosh" stroke-width="1.6" d="M0 31 C55 19 110 39 159 25"/>
    <text class="wordmark wordmark--light" x="8" y="12" font-size="6">wandervelo.net</text>
    <text class="detail" x="100" y="8" font-size="2.6">Office address line</text>
    <text class="detail" x="100" y="12" font-size="2.6">Phone and fax</text>
    <text class="detail" x="100" y="16" font-size="2.6">Web address</text>
  </g>

  <!-- Compliment slip -->
  <g class="compliment-slip" transform="translate(703,60)">
    <rect class="paper" width="175" height="94"/>
    <path class="green" d="M0 0 H175 V22 C120 34 60 14 0 28 Z"/>
    <path class="swoosh" stroke-width="1.4" d="M0 31 C60 19 120 39 175 25"/>
    <text class="wordmark wordmark--light" x="8" y="12" font-size="6">wandervelo.net</text>
  </g>

  <!-- DL envelope -->
  <g class="envelope envelope--dl" transform="translate(703,175)">
    <rect class="paper" width="175" height="84"/>
    <path class="green" d="M0 0 H175 V18 C120 30 60 10 0 24 Z"/>
    <path class="swoosh" stroke-width="1.4" d="M0 27 C60 15 120 35 175 21"/>
    <text class="wordmark wordmark--light" x="8" y="11" font-size="6">wandervelo.net</text>
  </g>

  <!-- Envelope, front -->
  <g class="envelope envelope--front" transform="translate(948,113)">
    <rect class="paper" width="199" height="60"/>
    <path class="green" d="M0 0 H199 V14 C140 26 70 6 0 20 Z"/>
    <path class="swoosh" stroke-width="1.4" d="M0 23 C70 11 140 31 199 17"/>
    <text class="wordmark wordmark--light" x="8" y="10" font-size="6">wandervelo.net</text>
  </g>

  <!-- Envelope, back with flap -->
  <g class="envelope envelope--back" transform="translate(948,176)">
    <rect class="paper" width="199" height="90"/>
    <path class="green" d="M0 0 H199 L99.5 38 Z"/>
    <path class="flap-line" d="M0 90 L90 40 M199 90 L109 40"/>
  </g>

</svg>
</body>
</html>
```